Music Industry Business Needs a Business Card Design

Copper Lantern is an audio mastering company that has been in business for 20 years. Mastering is the final creative step in the music production chain. Our job is to make the music sound as good as it possibly can prior to release to the public. Our world is technical, artistic, precise. We work on everything from independent artists to the music for the Grandfield Cup. We are looking for a new, more modern business card design. I am uploading a copy of our logo, although it doesn't absolutely need to be included in the design.

Target Market(s)

Music Industry Professionals

Industry/Entity Type

Business

Contact Information for Business Card

Address, Phone, Email, Website, Name, Job Title

Font styles to use
Sans Serif

Requirements
Must have
• Sorry, but I don't have any concrete things to request. If I had a clear idea of what I want, I would probably just design something myself. I am looking for fresh input and thought I would try this.
Should not have
• Anything that is typical, such as headphones or the like.

```html
<!DOCTYPE html>
<html lang="en">
<head>
<meta charset="utf-8">
<title>Copper Lantern – Business Card</title>
<link href="https://fonts.googleapis.com/css2?family=Open+Sans:wght@300;400;600&display=swap" rel="stylesheet">
<style>
  :root {
    --page: #ffffff;
    --card-front: #222222;
    --card-back: #000000;
    --ink: #ffffff;
    --shadow: rgba(0, 0, 0, 0.35);
    --red: #e8323c;
    --magenta: #b23c9c;
    --teal: #5fc4b4;
    --yellow: #f2c21c;
    --pink: #e8407a;
    --social-blue: #3b5a9a;
    --social-teal: #1f77a8;
    --social-orange: #ec7a1c;
  }
  * { margin: 0; padding: 0; box-sizing: border-box; }
  html, body {
    width: 1200px; height: 402px; overflow: hidden;
    background: var(--page);
    font-family: "Open Sans", Arial, sans-serif;
    color: var(--ink);
  }
  .canvas { position: relative; width: 1200px; height: 402px; }
  .card {
    position: absolute; top: 18px; width: 574px; height: 365px;
    overflow: hidden; box-shadow: 3px 4px 6px var(--shadow);
  }
  .card--front { left: 18px; background: var(--card-front); }
  .card--back { left: 610px; background: var(--card-back); }

  .spectrum-streaks { position: absolute; left: 0; top: 0; }
  .floor-glow {
    position: absolute; left: 180px; top: 230px; width: 420px; height: 160px;
    background: radial-gradient(ellipse at 60% 40%, rgba(255,255,255,0.10), rgba(255,255,255,0) 65%);
  }

  .brand-name {
    position: absolute; left: 34px; top: 93px;
    font-weight: 400; font-size: 25px; letter-spacing: 0.5px; white-space: nowrap;
  }
  .identity { position: absolute; left: 34px; top: 186px; }
  .identity__name, .identity__role { font-weight: 600; font-size: 18px; line-height: 33px; }
  .address { position: absolute; left: 34px; top: 252px; font-size: 15.5px; line-height: 29.5px; }
  .contacts { position: absolute; left: 286px; top: 252px; list-style: none; font-size: 15.5px; line-height: 29.5px; }
  .contacts li { display: flex; align-items: center; height: 29.5px; }
  .contacts svg { width: 24px; height: 24px; margin-right: 23px; flex: none; }

  .equalizer { position: absolute; left: 0; top: 0; }
  .back-title {
    position: absolute; left: 0; right: 0; top: 152px; text-align: center;
    font-weight: 300; font-size: 47px; letter-spacing: 0.5px; white-space: nowrap;
    padding-left: 40px;
  }
  .socials { position: absolute; left: 68px; top: 240px; display: flex; gap: 32px; }
  .social {
    width: 55px; height: 55px; border-radius: 4px;
    display: flex; align-items: center; justify-content: center;
    font-weight: 600; font-size: 13px;
  }
  .social--tribe { background: var(--social-blue); }
  .social--nexo { background: var(--social-teal); }
  .social--feed { background: var(--social-orange); }
</style>
</head>
<body>
<main class="canvas">

  <section class="card card--front" aria-label="Card front">
    <svg class="spectrum-streaks" width="574" height="365" role="img" aria-label="Diagonal streaks of multicoloured equalizer blocks">
      <defs>
        <linearGradient id="streakFill" x1="0" y1="0" x2="1" y2="0">
          <stop offset="0" stop-color="#e8407a"/>
          <stop offset="0.25" stop-color="#6ab83c"/>
          <stop offset="0.5" stop-color="#5fb8e0"/>
          <stop offset="0.75" stop-color="#f29a1c"/>
          <stop offset="1" stop-color="#9a5ab4"/>
        </linearGradient>
      </defs>
      <polygon points="400,0 574,0 574,40 520,205 470,195 440,120 340,170" fill="url(#streakFill)" opacity="0.9"/>
    </svg>
    <div class="floor-glow" role="img" aria-label="Soft dotted light wave"></div>

    <div class="brand-name">COPPER LANTERN</div>

    <div class="identity">
      <p class="identity__name">Name</p>
      <p class="identity__role">Position</p>
    </div>

    <address class="address" style="font-style:normal">
      518 - 12th Avenue N.W.<br>
      Westbrook, Ontario, Canada<br>
      K7R 3M2
    </address>

    <ul class="contacts">
      <li>
        <svg viewBox="0 0 24 24" fill="none" stroke="#fff" stroke-width="1.5">
          <circle cx="12" cy="12" r="10.5"/>
          <path d="M8.5 6.5l2 2-1.2 1.5c.8 1.8 2 3 3.7 3.8l1.5-1.2 2 2-1.3 1.6c-3.8-.6-7.3-4.1-7.9-7.9z" fill="#fff" stroke="none"/>
        </svg>(555) 318 - 4092
      </li>
      <li>
        <svg viewBox="0 0 24 24" fill="none" stroke="#fff" stroke-width="1.4">
          <rect x="2" y="5.5" width="20" height="13"/>
          <path d="M2 5.5l10 7.5 10-7.5"/>
        </svg>info@www.copperlantern.ca
      </li>
      <li>
        <svg viewBox="0 0 24 24" fill="none" stroke="#fff" stroke-width="1.4">
          <circle cx="12" cy="12" r="10"/>
          <ellipse cx="12" cy="12" rx="4.5" ry="10"/>
          <path d="M2 12h20M4 6.5h16M4 17.5h16"/>
        </svg>www.copperlantern.ca
      </li>
    </ul>
  </section>

  <section class="card card--back" aria-label="Card back">
    <svg class="equalizer" width="574" height="365" aria-hidden="true">
      <defs>
        <linearGradient id="fade" x1="0" y1="0" x2="0" y2="1">
          <stop offset="0" stop-color="#fff" stop-opacity="0.95"/>
          <stop offset="0.8" stop-color="#fff" stop-opacity="0.55"/>
          <stop offset="1" stop-color="#fff" stop-opacity="0"/>
        </linearGradient>
        <mask id="barMask"><rect width="574" height="330" fill="url(#fade)"/></mask>
      </defs>
      <g mask="url(#barMask)">
        <rect x="68" y="72" width="68" height="258" fill="var(--red)"/>
        <rect x="140" y="137" width="70" height="193" fill="var(--magenta)"/>
        <rect x="212" y="104" width="70" height="226" fill="var(--teal)"/>
        <rect x="287" y="75" width="70" height="255" fill="var(--yellow)"/>
        <rect x="362" y="135" width="68" height="195" fill="var(--red)"/>
        <rect x="436" y="47" width="68" height="283" fill="var(--pink)"/>
      </g>
    </svg>
    <div class="back-title">COPPER LANTERN</div>
    <div class="socials">
      <div class="social social--tribe">Tribe</div>
      <div class="social social--nexo">Nexo</div>
      <div class="social social--feed">Feed</div>
    </div>
  </section>

</main>
</body>
</html>
```